The Council for Stewardship in Civic Works' 2024 Rise Together Summit: Spark Venture needs a full page flyer that can be converted to a website header.

Date: February, 16, 2024
Location: Harborlight Meeting Pavilion, Larkmoor, TX

ABOUT THE FORUM

Dedicated to celebrating the entrepreneurial spirit and unwavering determination of women, the Rise Together Summit proudly presents, “Spark Venture.” Here, we believe in the power of dreams, the strength of innovation, and the impact of women-led endeavors.

Join us at this dynamic Forum as we explore the world of Spark Ventures – those inspiring ventures, including YOURSELF, fueled by creativity, ambition, and a deep-seated love for what we do. Whether you're an seasoned expert, a budding visionary, or simply an enthusiast eager to learn and grow, this Forum is your hub for all things related to the fusion of passion and business.

WHAT TO EXPECT

Inspiring Stories: Immerse yourself in a collection of captivating success stories and personal journeys that highlight the incredible feats achieved through passion-driven initiatives. Learn from remarkable women who turned their dreams into reality and gain insights into their strategies, challenges, and triumphs.

Expert Insights: Discover the art of transforming a passion into a sustainable business model. Our forum gathers experts and thought leaders across the AEC community (and more) to share invaluable advice, practical tips, and proven strategies, guiding you along the exciting journey of pursuing your passion.

Networking Opportunities: Connect with like-minded individuals who share your passion for making a difference. Engage in lively discussions, exchange ideas, and build meaningful relationships with fellow forum participants, potential collaborators, and mentors who can help elevate your Spark Venture.

Interactive Workshops: Participate in hands-on workshops designed to enhance your skills, from refining your business plan to mastering effective marketing techniques. These immersive sessions are tailored to address the unique challenges faced by women in the design and construction industry and will empower you to overcome obstacles with confidence.

Passion Showcase: Elevate your project's visibility by showcasing your Spark Venture to the Forum. Receive feedback, support, and perhaps even connect with individuals who are excited to collaborate and join you on your journey.

Empowerment and Support: Embrace a supportive community that believes in your potential and is committed to fostering an inclusive environment. Share your highs and lows, seek advice, and find encouragement to keep pursuing your passion, no matter the hurdles.

Join Us!

Whether you're taking your first steps toward transforming your passion into a business or are seeking to amplify the impact of your existing venture, or just personal improvement, the Rise Together Summit: "Spark Venture" is your gateway to inspiration, knowledge, and connection. Let's come together, celebrate the strength of women-led endeavors, and empower one another to turn our passions into legacies that shape the future.

Target Market(s)

Professionals in the design and construction industry.

Industry/Entity Type

Design and Construction

Requirements
Must have
• C-SwCW logo
Nice to have
• Title, Date, Location, Graphics that fit the theme of the the Forum: Spark Venture, and the mission of the organization.
Should not have
• Full description of event should be in the graphic.

```html
<!DOCTYPE html>
<html lang="en">
<head>
<meta charset="UTF-8">
<title>Rise Together Summit 2024 – Flyer</title>
<link href="https://fonts.googleapis.com/css2?family=Oswald:wght@700&family=Poppins:wght@400;500;600;700;800&display=swap" rel="stylesheet">
<style>
  :root {
    --blue: #2b4aa0;
    --blue-deep: #1d3f94;
    --green: #8ab43f;
    --grey-text: #55575b;
    --ink: #141414;
    --paper: #ffffff;
    --stage: #e9eaec;
    --haze: #e4e5e8;
  }
  * { box-sizing: border-box; margin: 0; padding: 0; }
  html, body {
    width: 1200px; height: 2389px; overflow: hidden;
    background: var(--stage);
    font-family: "Poppins", sans-serif;
  }
  .flyer {
    position: absolute; left: 60px; top: 496px;
    width: 1080px; height: 1397px;
    background: var(--paper);
    overflow: hidden;
    box-shadow: 0 6px 18px rgba(0,0,0,0.18);
  }
  .hero-art {
    position: absolute; left: 600px; top: 0; width: 480px; height: 1180px;
    background: linear-gradient(180deg, var(--haze) 0%, #d7dae2 35%, #6f83bd 65%, var(--blue-deep) 100%);
    border-top-left-radius: 240px;
  }
  .brand { position: absolute; left: 50px; top: 48px; display: flex; align-items: center; gap: 22px; }
  .brand-mark { width: 96px; height: 96px; background: var(--green); flex: none; }
  .brand-name { font-weight: 600; font-size: 34px; line-height: 1.15; color: var(--grey-text); }
  .title { position: absolute; left: 46px; top: 196px; }
  .title-year { font-family: "Oswald", sans-serif; font-weight: 700; font-size: 160px; line-height: 1; color: var(--ink); letter-spacing: -2px; }
  .title-line { font-weight: 800; line-height: 1; letter-spacing: -1px; }
  .title-rise { font-size: 92px; color: var(--grey-text); margin-top: 10px; }
  .title-together { font-size: 104px; color: var(--blue); margin-top: 14px; }
  .title-summit { font-size: 116px; color: var(--green); margin-top: 14px; }
  .date-banner {
    position: absolute; left: 25px; top: 710px; width: 582px; height: 72px;
    background: var(--blue); color: #fff;
    border-radius: 36px 18px 36px 18px;
    transform: skewX(-12deg);
    box-shadow: 0 8px 10px rgba(0,0,0,0.18);
    display: flex; align-items: center; justify-content: center;
  }
  .date-banner span { transform: skewX(12deg); font-weight: 700; font-size: 48px; }
  .date-banner sup { font-size: 26px; }
  .location { position: absolute; left: 46px; top: 826px; display: flex; gap: 14px; font-weight: 600; font-size: 25px; line-height: 1.12; color: #1e1e1e; }
  .location svg { flex: none; margin-top: 4px; }
  .expect-heading { position: absolute; left: 43px; top: 908px; font-weight: 700; font-size: 30px; color: var(--blue); }
  .expect-list { position: absolute; left: 43px; top: 960px; width: 560px; list-style: none; display: grid; grid-template-columns: 285px 275px; row-gap: 16px; }
  .expect-list li { display: flex; gap: 14px; font-size: 21px; line-height: 1.12; color: #222; }
  .expect-list svg { flex: none; margin-top: 3px; }
  .footer-wave { position: absolute; left: 0; top: 1110px; width: 1080px; height: 287px; }
  .contact { position: absolute; left: 43px; top: 1205px; color: #fff; }
  .contact h2 { font-weight: 700; font-size: 30px; color: var(--blue); margin-bottom: 8px; }
  .contact p { display: flex; align-items: center; gap: 14px; font-size: 21px; line-height: 1.5; }
  .join { position: absolute; left: 505px; top: 1168px; width: 545px; }
  .join h2 { font-weight: 700; font-size: 30px; color: var(--blue); margin-bottom: 10px; }
  .join p { border-left: 2px solid #fff; padding-left: 16px; color: #fff; font-size: 16px; line-height: 1.2; }
</style>
</head>
<body>
<main class="flyer">
  <div class="hero-art" role="img" aria-label="Illustration of a businesswoman silhouette walking with a briefcase in front of pale city towers"></div>

  <header class="brand">
    <div class="brand-mark"></div>
    <div class="brand-name">Council for Stewardship<br>in Civic Works</div>
  </header>

  <h1 class="title">
    <div class="title-year">2024</div>
    <div class="title-line title-rise">RISE</div>
    <div class="title-line title-together">TOGETHER</div>
    <div class="title-line title-summit">SUMMIT</div>
  </h1>

  <div class="date-banner"><span>16<sup>th</sup> FEBRUARY, 2024</span></div>

  <div class="location">
    <svg width="22" height="30" viewBox="0 0 22 30"><path d="M11 1a10 10 0 0 0-10 10c0 7 10 18 10 18s10-11 10-18A10 10 0 0 0 11 1z" fill="var(--blue)"/><circle cx="11" cy="11" r="4" fill="#fff"/></svg>
    <div>Harborlight Meeting Pavilion,<br>Larkmoor, TX</div>
  </div>

  <h2 class="expect-heading">WHAT TO EXPECT</h2>
  <ul class="expect-list">
    <li><svg width="16" height="16" viewBox="0 0 16 16"><circle cx="8" cy="8" r="8" fill="var(--green)"/><path d="M4.5 8.2l2.4 2.3 4.6-4.8" stroke="#fff" stroke-width="1.8" fill="none"/></svg>Inspiring Stories</li>
    <li><svg width="16" height="16" viewBox="0 0 16 16"><circle cx="8" cy="8" r="8" fill="var(--green)"/><path d="M4.5 8.2l2.4 2.3 4.6-4.8" stroke="#fff" stroke-width="1.8" fill="none"/></svg>Interactive Workshops</li>
    <li><svg width="16" height="16" viewBox="0 0 16 16"><circle cx="8" cy="8" r="8" fill="var(--green)"/><path d="M4.5 8.2l2.4 2.3 4.6-4.8" stroke="#fff" stroke-width="1.8" fill="none"/></svg>Expert Insights</li>
    <li><svg width="16" height="16" viewBox="0 0 16 16"><circle cx="8" cy="8" r="8" fill="var(--green)"/><path d="M4.5 8.2l2.4 2.3 4.6-4.8" stroke="#fff" stroke-width="1.8" fill="none"/></svg>Passion Showcase</li>
    <li><svg width="16" height="16" viewBox="0 0 16 16"><circle cx="8" cy="8" r="8" fill="var(--green)"/><path d="M4.5 8.2l2.4 2.3 4.6-4.8" stroke="#fff" stroke-width="1.8" fill="none"/></svg>Networking<br>Opportunities</li>
    <li><svg width="16" height="16" viewBox="0 0 16 16"><circle cx="8" cy="8" r="8" fill="var(--green)"/><path d="M4.5 8.2l2.4 2.3 4.6-4.8" stroke="#fff" stroke-width="1.8" fill="none"/></svg>Empowerment and<br>Support</li>
  </ul>

  <svg class="footer-wave" viewBox="0 0 1080 287" preserveAspectRatio="none">
    <path d="M0 65 Q540 -30 1080 55 L1080 287 L0 287 Z" fill="var(--blue)"/>
    <path d="M0 76 Q540 -8 1080 70 L1080 287 L0 287 Z" fill="var(--green)"/>
  </svg>

  <section class="contact">
    <h2>CONTACT US</h2>
    <p><svg width="20" height="20" viewBox="0 0 20 20"><circle cx="10" cy="10" r="10" fill="var(--blue)"/><path d="M6.5 5.5l2 2-1 1.3a6 6 0 0 0 3.7 3.7l1.3-1 2 2-1.3 1.3c-3.6 0-7.9-4.3-7.9-7.9z" fill="#fff"/></svg>(512) 555-0148</p>
    <p><svg width="20" height="20" viewBox="0 0 20 20"><circle cx="10" cy="10" r="10" fill="var(--blue)"/><rect x="5" y="6.5" width="10" height="7" fill="#fff"/><path d="M5 6.5l5 4 5-4" stroke="var(--blue)" stroke-width="1.2" fill="none"/></svg>dana.whitfield@c-swcw.org</p>
    <p><svg width="20" height="20" viewBox="0 0 20 20"><circle cx="10" cy="10" r="10" fill="var(--blue)"/><circle cx="10" cy="10" r="5.5" stroke="#fff" stroke-width="1.2" fill="none"/><ellipse cx="10" cy="10" rx="2.3" ry="5.5" stroke="#fff" stroke-width="1.1" fill="none"/><path d="M4.5 10h11" stroke="#fff" stroke-width="1.1"/></svg>www.c-swcw.example.org</p>
  </section>

  <section class="join">
    <h2>JOIN US!</h2>
    <p>Whether you’re taking your first steps toward transforming your passion into a business or are seeking to amplify the impact of your existing venture, or just personal improvement, the Rise Together Summit: “Spark Venture” is your gateway to inspiration, knowledge, and connection. Let’s come together, celebrate the strength of women-led endeavors, and empower one another to turn our passions into legacies that shape the future.</p>
  </section>
</main>
</body>
</html>
```